We currently have a good logo and we want business cards that can display our logo but also represent our industry - telecom construction - We are a construction company specializing in telecom construction such as installation of fiber optic cable throughout cities and across the country. Nationwide services
We are large enough to handle most any project yet small enough to be a flexible partner and resource.

Target Market(s)

U.S. based telecom carriers and providers

Industry/Entity Type

Construction

Contact Information for Business Card

Business cards should include our logo, phone number and website address. Also, including some information as to our core services would be good.

Colors

Designer to choose colors to be used in the design.

Requirements
Must have
• Colors based on logo
• Must use our logo
• Logo, name, email, website address, phone number
• Tovasco Conduit
• Brent Halvik
• Director of Business Development
• (555) 271-0386
• www.TVSQ-example.com
Nice to have
• Construction services including:
• Small Cell Construction
• Boring/Drilling
• Plowing / Trenching
• Conduit installation
• Fiber pulling
• splicing
• building entries
• Aerial construction
• Aerial Make Ready
• Make Ready Engineering
Should not have
• We are open to ideas

```html
<!DOCTYPE html>
<html lang="en">
<head>
<meta charset="utf-8">
<title>Tovasco Conduit – Business Card</title>
<link href="https://fonts.googleapis.com/css2?family=Ubuntu:wght@500;700&family=Lato:wght@300;400&display=swap" rel="stylesheet">
<style>
  :root {
    --page-bg: #dedede;
    --card-white: #ffffff;
    --brand-blue: #0e4fa6;
    --back-blue: #2b5aa7;
    --back-blue-deep: #234d98;
    --text-grey: #8a8a8a;
    --white: #ffffff;
  }
  * { margin: 0; padding: 0; box-sizing: border-box; }
  html, body { width: 1200px; height: 960px; overflow: hidden; }
  body { background: var(--page-bg); position: relative; font-family: "Lato", sans-serif; }

  .card {
    position: absolute;
    left: 281px;
    width: 655px;
    border-radius: 20px;
    overflow: hidden;
  }
  .card--front { top: 80px; height: 374px; background: var(--card-white); }
  .card--back { top: 506px; height: 376px; background: var(--back-blue); }

  /* Front */
  .front-brand {
    position: absolute; left: 425px; top: 68px; width: 180px;
    font-family: "Ubuntu", sans-serif; font-weight: 700; font-size: 34px;
    line-height: 38px; color: var(--brand-blue); text-align: center;
  }
  .holder-name {
    position: absolute; left: 68px; top: 143px;
    font-family: "Ubuntu", sans-serif; font-weight: 500; font-size: 27px;
    line-height: 34px; color: var(--brand-blue);
  }
  .holder-title {
    position: absolute; left: 68px; top: 178px;
    font-weight: 400; font-size: 17.5px; line-height: 22px; color: var(--text-grey);
  }
  .contact-line {
    position: absolute; left: 68px;
    display: flex; align-items: center; gap: 7px;
    font-weight: 400; font-size: 17.5px; line-height: 22px; color: var(--text-grey);
    white-space: nowrap;
  }
  .contact-line--phone { top: 226px; }
  .contact-line--email { top: 250px; }
  .contact-line svg { width: 14px; height: 14px; fill: var(--brand-blue); flex: none; }

  .web-band {
    position: absolute; left: 0; top: 280px; width: 300px; height: 30px;
    background: var(--brand-blue); color: var(--white);
    font-weight: 400; font-size: 17.5px; line-height: 30px; padding-left: 68px;
    white-space: nowrap;
  }
  .drill-bit {
    position: absolute; left: 296px; top: 252px; width: 125px; height: 85px;
    background: linear-gradient(90deg, #9a9a9a, #6f6f6f 60%, #8e8e8e);
    border-radius: 6px 20px 20px 6px;
  }

  /* Back */
  .back-photo {
    position: absolute; inset: 0;
    background: linear-gradient(180deg, var(--back-blue-deep) 0%, var(--back-blue) 45%, var(--back-blue) 100%);
  }
  .back-brand {
    position: absolute; left: 0; right: 0; top: 92px;
    font-family: "Ubuntu", sans-serif; font-weight: 700; font-size: 54px;
    line-height: 62px; color: var(--white); text-align: center;
  }
  .service-list {
    position: absolute; left: 0; right: 0; top: 249px;
    color: var(--white); font-size: 18.5px; line-height: 23.5px; text-align: center;
    list-style: none; white-space: nowrap;
  }
  .service-list li span + span::before { content: "•"; margin: 0 2px 0 12px; }
  .service-list li span:first-child::before { content: "•"; margin-right: 2px; }
</style>
</head>
<body>

<section class="card card--front">
  <div class="front-brand">Tovasco Conduit</div>
  <h1 class="holder-name">Brent Halvik</h1>
  <p class="holder-title">Director of Business Development</p>
  <p class="contact-line contact-line--phone">
    <svg viewBox="0 0 16 16" aria-hidden="true"><path d="M3 1 6 4 4.5 6c1 2 3 4 5.5 5.5L12 10l3 3-2 2C7 14 2 9 1 3Z"/></svg>
    (555) 271-0386
  </p>
  <p class="contact-line contact-line--email">
    <svg viewBox="0 0 16 16" aria-hidden="true"><path d="M1 3h14v10H1Z M2 4l6 5 6-5" stroke="#fff" stroke-width="1"/></svg>
    info@TVSQ-example.com
  </p>
  <div class="web-band">www.TVSQ-example.com</div>
  <div class="drill-bit" role="img" aria-label="Drill bit illustration at the end of the web address band"></div>
</section>

<section class="card card--back">
  <div class="back-photo" role="img" aria-label="Photo of a work truck and crew at a roadside drilling site, tinted blue"></div>
  <div class="back-brand">Tovasco<br>Conduit</div>
  <ul class="service-list">
    <li><span>Small Cell Construction</span><span>Boring/Drilling</span><span>Plowing / Trenching</span></li>
    <li><span>Conduit installation</span><span>Fiber pulling</span><span>splicing</span><span>building entries</span></li>
    <li><span>Aerial construction</span><span>Aerial Make Ready</span><span>Make Ready Engineering</span></li>
  </ul>
</section>

</body>
</html>
```